Packaging Design for Snack Food Company

Our company is Crumb Harbour (www.crumbharbour.com.au). We import and manufacturer a range of snack foods which are sold throughout Australia.

Our range of snacks can be viewed at www.crumbharbour.com.au. Currently we use a plain bag with a label but we want to move to a bag with a graphic design.

We have a few basic requirements.
1. Bag material is 50um polypropylene.
2. Bag size is 475mm width x 350mm length (see attached photo of drawing for more info).
3. We want a clear window on the front and back of the bag.
4. Front side must have our logo (see attached image). We are open to a new logo design if you can think of something better than our current one.
5. Back side must have space (85mm x 60mm) for printing ingredients, nutritional information, bar code & expiry date and have our address & contact information.
6. Top and bottom of the bag must be opaque to hide the product, the window can be positioned somewhere in the centre of the bag.
7. We want to use only one bag across our range of snacks. Our packing machine will print on the front side clear window what each product is ie. Cracker Mix Nacho Cheese 160g and on the back it will print the ingredients and nutritional info etc.

Our logo is in the files below along with some design ideas.

UPDATE 3/8/16
Some great designs have been submitted so far. Thank you. We have now
guaranteed the projected so we are committed to purchasing a design.

Industry/Entity Type

It Company

Requirements
Must have
• No must haves, we are open to any design ideas.

```html
<!DOCTYPE html>
<html lang="en">
<head>
<meta charset="utf-8">
<title>Crumb Harbour – Cracker Mix Nacho Cheese</title>
<link rel="stylesheet" href="https://fonts.googleapis.com/css2?family=Kaushan+Script&family=Great+Vibes&family=Roboto+Condensed:wght@400;700&display=swap">
<style>
  :root {
    --maroon: #7a0a16;
    --red: #c41d27;
    --orange: #f7742a;
    --yellow: #fdd35a;
    --teal: #45bfbb;
    --gold: #e2c67a;
    --white: #ffffff;
    --wine: #8a0f1c;
    --crimson: #d4141f;
    --ink: #2a2a2a;
  }
  * { margin: 0; padding: 0; box-sizing: border-box; }
  html, body { width: 814px; height: 1200px; overflow: hidden; background: var(--maroon); }
  .pack { position: relative; width: 814px; height: 1200px; overflow: hidden; }
  .pack-art { position: absolute; inset: 0; display: block; }

  .brand-name {
    position: absolute; left: 90px; top: 210px; width: 560px;
    font-family: "Kaushan Script", cursive; font-weight: 400;
    color: var(--white); font-size: 112px; line-height: 0.95;
    transform: rotate(-8deg); transform-origin: left top;
  }
  .brand-name .line-two { display: block; padding-left: 170px; }

  .tagline {
    position: absolute; font-family: "Great Vibes", cursive;
    color: var(--white); font-size: 52px; line-height: 1;
    transform: rotate(-16deg); transform-origin: left center;
  }
  .tagline-delicious { left: 192px; top: 960px; }
  .tagline-healthy { left: 262px; top: 1030px; }

  .product-label {
    position: absolute; left: 436px; top: 716px; width: 328px; height: 328px;
    border-radius: 50%; background: var(--white); text-align: center;
  }
  .product-range {
    margin-top: 60px; font-family: "Kaushan Script", cursive;
    color: var(--crimson); font-size: 38px; line-height: 1;
  }
  .product-flavour {
    margin-top: 14px; font-family: "Kaushan Script", cursive;
    color: var(--wine); font-size: 48px; line-height: 1; white-space: nowrap;
  }
  .product-rule {
    width: 272px; margin: 30px auto 0; border-top: 2px dotted var(--crimson);
  }
  .net-weight {
    margin-top: 28px; font-family: "Roboto Condensed", sans-serif;
    color: var(--ink); font-size: 22px;
  }
  .net-weight strong { font-size: 34px; font-weight: 700; }
</style>
</head>
<body>
<main class="pack">
  <svg class="pack-art" width="814" height="1200" viewBox="0 0 814 1200" aria-hidden="true">
    <defs>
      <radialGradient id="sunburst" cx="330" cy="380" r="560" gradientUnits="userSpaceOnUse">
        <stop offset="0" stop-color="var(--yellow)"/>
        <stop offset="0.45" stop-color="var(--orange)"/>
        <stop offset="1" stop-color="var(--red)"/>
      </radialGradient>
      <radialGradient id="lowerGlow" cx="414" cy="1100" r="360" gradientUnits="userSpaceOnUse">
        <stop offset="0" stop-color="#f99a3a"/>
        <stop offset="0.5" stop-color="#e1412a"/>
        <stop offset="1" stop-color="#b81a26"/>
      </radialGradient>
      <linearGradient id="goldSheen" x1="0" y1="0" x2="1" y2="0">
        <stop offset="0" stop-color="#c9a24e"/>
        <stop offset="0.5" stop-color="#f6e6b0"/>
        <stop offset="1" stop-color="#c9a24e"/>
      </linearGradient>
      <linearGradient id="snackTones" x1="0" y1="0" x2="1" y2="1">
        <stop offset="0" stop-color="#f3dfa8"/>
        <stop offset="0.5" stop-color="#e6c07a"/>
        <stop offset="1" stop-color="#f1d9a4"/>
      </linearGradient>
    </defs>

    <rect class="band-base" width="814" height="1200" fill="var(--maroon)"/>
    <rect class="field-sunburst" y="78" width="814" height="1018" fill="url(#sunburst)"/>

    <path class="wave-teal" fill="var(--teal)"
      d="M0,552 C120,612 270,600 420,482 C560,380 700,356 814,344 L814,480 C640,476 500,480 420,504 C260,560 150,700 0,780 Z"/>

    <rect class="side-strip" y="1010" width="814" height="34" fill="var(--teal)"/>

    <g role="img" aria-label="Clear window showing the potato crackers inside">
      <path class="window-clear" fill="url(#snackTones)"
        d="M0,772 C150,700 260,560 420,500 C560,462 700,468 814,472 L814,1016 L0,1016 Z"/>
    </g>
    <path class="window-rim" fill="none" stroke="url(#goldSheen)" stroke-width="10"
      d="M0,772 C150,700 260,560 420,500 C560,462 700,468 814,472"/>

    <path class="lower-dome" fill="url(#lowerGlow)" stroke="url(#goldSheen)" stroke-width="10"
      d="M56,1100 C56,900 240,800 414,800 C588,800 772,900 772,1100 Z"/>

    <rect class="band-top" width="814" height="74" fill="var(--maroon)"/>
    <rect class="rule-top" y="74" width="814" height="4" fill="url(#goldSheen)"/>
    <rect class="band-bottom" y="1096" width="814" height="104" fill="var(--maroon)"/>
    <rect class="rule-bottom" y="1094" width="814" height="4" fill="url(#goldSheen)"/>
  </svg>

  <h1 class="brand-name">Crumb<span class="line-two">Harbour</span></h1>

  <p class="tagline tagline-delicious">Delicious...</p>
  <p class="tagline tagline-healthy">Healthy...</p>

  <section class="product-label">
    <p class="product-range">Cracker Mix</p>
    <p class="product-flavour">Nacho Cheese</p>
    <div class="product-rule"></div>
    <p class="net-weight">Net Wt : <strong>160</strong>gm</p>
  </section>
</main>
</body>
</html>
```